Bramwell Resources Ltd. - Refreshed business card challenge

A revised, refreshed business card design for my oil and gas company using my existing logo. Feel free to be as creative as you like!

Target Market(s)

bankers, lawyers

Industry/Entity Type

Oil And Gas Exploration

Contact Information for Business Card

See the "Must Haves" section

Font styles to use
Serif
Sans Serif

Colors

Designer to choose colors to be used in the design.

Requirements
Must have
• Existing business logo, name, title, email, phone number, business address
• Neil Hadley, CA, CPA
• Vice President Finance & Chief Financial Officer
• nhadley@bramwellresources-mail.com
• office: (587)555-0142
• cell: (403)555-0187
• 1400, 815 4 Street S.W.
• Calgary, AB
• T2P 4K8
Should not have
• Should not be plain and boring.

```html
<!DOCTYPE html>
<html lang="en">
<head>
<meta charset="utf-8">
<title>Bramwell Resources – Business Card</title>
<link href="https://fonts.googleapis.com/css2?family=Roboto:wght@400;700&display=swap" rel="stylesheet">
<style>
  :root {
    --backdrop: #d6d6d6;
    --card-white: #ffffff;
    --forest: #0d5a3a;
    --forest-deep: #004a2c;
    --forest-light: #0f6a45;
    --earth: #6b3a1f;
    --rule-grey: #8c8c8c;
    --ink: #3a3a3a;
  }
  html, body {
    margin: 0;
    padding: 0;
    width: 1200px;
    height: 951px;
    overflow: hidden;
    background: var(--backdrop);
    font-family: "Roboto", Arial, sans-serif;
  }
  .canvas {
    position: relative;
    width: 1200px;
    height: 951px;
  }
  .card {
    position: absolute;
    top: 327px;
    width: 520px;
    height: 297px;
    box-shadow: 0 10px 24px rgba(0,0,0,0.18);
    overflow: hidden;
  }
  .card--front { left: 60px; background: var(--card-white); }
  .card--back {
    left: 620px;
    background: radial-gradient(ellipse at 60% 35%, var(--forest-light), var(--forest) 55%, var(--forest-deep));
  }
  .contact {
    position: absolute;
    right: 265px;
    top: 42px;
    text-align: right;
    color: var(--ink);
  }
  .contact__name {
    margin: 0;
    font-size: 24px;
    font-weight: 700;
    color: var(--forest);
    letter-spacing: 0.3px;
  }
  .contact__title {
    margin: 2px 0 12px;
    font-size: 12px;
  }
  .contact__address {
    margin: 0 0 12px;
    font-size: 12px;
    line-height: 1.4;
    font-style: normal;
  }
  .contact__list {
    list-style: none;
    margin: 0;
    padding: 0;
    font-size: 12px;
    line-height: 1.55;
  }
  .contact__list li {
    display: flex;
    justify-content: flex-end;
    align-items: center;
    gap: 8px;
  }
  .contact__icon { width: 10px; height: 10px; }
  .dividers {
    position: absolute;
    left: 275px;
    top: 48px;
    display: flex;
    flex-direction: column;
    gap: 14px;
  }
  .dividers span { display: block; width: 2px; height: 42px; }
  .dividers .rule--grey { background: var(--rule-grey); }
  .dividers .rule--green { background: var(--forest); }
  .dividers .rule--brown { background: var(--earth); }
  .brand {
    position: absolute;
    display: flex;
    align-items: center;
    gap: 10px;
    font-weight: 700;
    line-height: 1;
    white-space: nowrap;
  }
  .brand__dot { width: 14px; height: 14px; border-radius: 50%; flex: none; }
  .card--front .brand { left: 292px; top: 210px; color: var(--forest); font-size: 20px; }
  .card--front .brand__dot { background: var(--forest); width: 12px; height: 12px; }
  .card--back .brand { left: 150px; top: 134px; color: var(--card-white); font-size: 30px; }
  .card--back .brand__dot { background: var(--card-white); }
</style>
</head>
<body>
<main class="canvas">
  <section class="card card--front" aria-label="Business card front">
    <div class="contact">
      <h1 class="contact__name">John Smith</h1>
      <p class="contact__title">Founder &amp; CEO</p>
      <address class="contact__address">2450 N. Alder Creek PKWY Ste. B<br>Brookfield, TX 75314</address>
      <ul class="contact__list">
        <li>123 456 7890
          <svg class="contact__icon" viewBox="0 0 10 10" aria-hidden="true"><rect x="2" y="0.5" width="6" height="9" rx="1" fill="var(--forest)"/></svg></li>
        <li>012 345 6789
          <svg class="contact__icon" viewBox="0 0 10 10" aria-hidden="true"><path d="M2 1 L4 1 L5 3 L4 4 Q5 6 6 6 L7 5 L9 6 L9 8 Q5 9 1 3 Z" fill="var(--forest)"/></svg></li>
        <li>info@yourdomain.com
          <svg class="contact__icon" viewBox="0 0 10 10" aria-hidden="true"><rect x="0.5" y="2" width="9" height="6" fill="var(--forest)"/><path d="M0.5 2 L5 5.5 L9.5 2" stroke="#fff" fill="none"/></svg></li>
        <li>www.yourdomain.com
          <svg class="contact__icon" viewBox="0 0 10 10" aria-hidden="true"><circle cx="5" cy="5" r="4.3" fill="var(--forest)"/><path d="M0.7 5 H9.3 M5 0.7 V9.3" stroke="#fff" stroke-width="0.8"/></svg></li>
      </ul>
    </div>
    <div class="dividers" aria-hidden="true">
      <span class="rule--grey"></span>
      <span class="rule--green"></span>
      <span class="rule--brown"></span>
    </div>
    <div class="brand"><span class="brand__dot"></span>Bramwell Resources</div>
  </section>

  <section class="card card--back" aria-label="Business card back">
    <div class="brand"><span class="brand__dot"></span>Bramwell Resources</div>
  </section>
</main>
</body>
</html>
```